ZolvantaRx -- Reshaping the Future

Redesign our B2B website using the current logo attached (zolvantarx-example.com).
Our company is based in New York.
ZolvantaRx is our company logo.
TWB logo represents our patent approved technology that serves our clients.
We are Affordability Program Administrators. Our clients are pharmaceutical manufacturers that sponsor affordability programs designed to attract consumers of their products (pharmaceutical medication) and prescribers (doctors that prescribe medication).
We oversee their programs by processing claims submitted by pharmacies and all sites of care for reimbursement (or rebates) on medication they purchased.
We want a new brand. We are open to changing the logo color.
See logos and an one-page overview attached.

Target Market(s)

pharmaceutical manufacturers

Industry/Entity Type

manufacturers of pharmaceuticals and other clinical products; life sciences

Number of Pages Required

5+ page

Font styles to use
Other font styles liked:
• Use the font used in the logo -- Cy. We currently use that with IBM Plex Sans. Open to changing IBM but keep CY.

Requirements
Must have
• Must appeal to pharmaceutical manufacturers; convey a level of sophistication; send a message of creativity and change
Nice to have
• simple -- easy to read messaging.
Should not have
• too many pictures of doctors or patients.

```html
<!DOCTYPE html>
<html lang="en">
<head>
<meta charset="utf-8">
<title>ZolvantaRx — Reshaping the Future of Healthcare</title>
<link href="https://fonts.googleapis.com/css2?family=IBM+Plex+Sans:wght@500;600;700&family=Karla:wght@400;500;700&display=swap" rel="stylesheet">
<style>
:root{
  --ink:#1f2a33;
  --dark:#25343d;
  --hero-a:#1d8fd6;
  --hero-b:#2c6fa8;
  --mission:#3a78b0;
  --teal:#21919a;
  --mint:#7fcfb6;
  --mint-soft:#a8dccb;
  --blue-seg:#4f76ad;
  --cta-blue:#5079b3;
  --cta-teal:#27979c;
  --grey-bg:#f3f4f6;
  --muted:#5a636b;
  --line:#d6dde3;
  --white:#ffffff;
}
*{box-sizing:border-box;margin:0;padding:0}
html,body{width:1200px;height:3663px;overflow:hidden}
body{position:relative;background:var(--white);font-family:"Karla",Arial,sans-serif;color:var(--ink)}
.abs{position:absolute}
h1,h2,h3,.brand,.btn{font-family:"IBM Plex Sans",Arial,sans-serif}

/* top bar */
.topbar{left:0;top:0;width:1200px;height:26px;background:linear-gradient(90deg,#1a8a72,#1c9ad6);color:#fff;font-size:11px;font-weight:700;text-align:center;line-height:26px}
.topbar a{color:#7fe0c9;text-decoration:none;margin-left:4px}

/* header */
.brand{font-weight:600;font-size:25px;color:var(--ink);display:flex;align-items:center;gap:8px}
.brand .dot{width:14px;height:14px;border-radius:50%;background:var(--teal)}
.util{top:43px;font-size:11px;font-weight:700;color:var(--ink)}
.soc{width:9px;height:9px;border-radius:50%;background:#2a8ad0;top:47px}
.nav{top:86px;font-size:13px;font-weight:700;color:var(--ink)}
.search{left:886px;top:86px;width:14px;height:14px}
.btn{display:flex;align-items:center;justify-content:center;font-size:13px;font-weight:600;border-radius:4px}
.btn-dark{background:var(--dark);color:#fff}

/* hero */
.hero{left:0;top:127px;width:1200px;height:538px;background:linear-gradient(100deg,var(--hero-a) 0%,#2a84c6 45%,var(--hero-b) 100%)}
.hero h1{position:absolute;left:166px;top:96px;width:480px;font-size:48px;line-height:55px;font-weight:600;color:#fff}
.hero p{position:absolute;left:166px;top:282px;width:330px;font-size:14.5px;line-height:22px;color:#e3f0fa}
.hero .btn{position:absolute;left:166px;top:371px;width:133px;height:47px}
.dashes{position:absolute;left:166px;top:483px;display:flex;gap:8px}
.dashes span{width:33px;height:2px;background:rgba(255,255,255,.55)}
.hero-photo{position:absolute;left:654px;top:51px;width:427px;height:487px;background:linear-gradient(160deg,#6aa6d6,#e9eef3 55%,#1f3b68);border-radius:180px 180px 0 0}
.vtext{font-size:8px;letter-spacing:2px;font-weight:700;writing-mode:vertical-rl;transform:rotate(180deg)}
.vline{width:1px;background:rgba(255,255,255,.5)}

/* about */
.about{left:0;top:665px;width:1200px;height:380px;background:var(--dark)}
.eyebrow{font-size:9px;font-weight:700;letter-spacing:2.5px}
.about .eyebrow{position:absolute;left:166px;top:89px;color:#cfd8de}
.about h2{position:absolute;left:166px;top:103px;width:360px;font-size:30px;line-height:39px;font-weight:500;color:#fff}
.about p{position:absolute;left:555px;top:88px;width:400px;font-size:12px;line-height:20px;color:#c8d2d8}
.about .btn{position:absolute;left:555px;top:245px;width:106px;height:44px;background:var(--mint-soft);color:var(--dark)}

/* services */
.services{left:0;top:1045px;width:1200px;height:771px;background:var(--grey-bg)}
.services h2{position:absolute;left:0;width:1200px;top:92px;text-align:center;font-size:36px;font-weight:600;color:var(--ink)}
.svc h3{font-size:16px;font-weight:600;color:var(--ink);margin-bottom:8px;line-height:21px}
.svc p{font-size:12px;line-height:20px;color:#39434b}
.svc.r{text-align:right}
.svc.c{text-align:center}
.skyline{left:0;top:575px;width:1200px;height:196px;background:linear-gradient(180deg,rgba(243,244,246,0),#dfe3e8 70%,#d4d9df)}

/* mission */
.mission{left:0;top:1816px;width:1200px;height:519px;background:linear-gradient(100deg,#2f6ea6,var(--mission) 60%,#3b7ab3)}
.mission-photo{position:absolute;left:156px;top:-12px;width:470px;height:531px;background:linear-gradient(180deg,#f2f4f6,#dde3ea 60%,#4a6d93);border-radius:200px 200px 0 0}
.mission .eyebrow{position:absolute;left:678px;top:106px;color:#d6e5f2}
.mission h2{position:absolute;left:678px;top:114px;width:420px;font-size:35px;line-height:43px;font-weight:500;color:#fff}
.mission p{position:absolute;left:678px;width:350px;font-size:12px;line-height:20px;color:#dbe8f3}

/* news */
.news-title{left:0;width:1200px;top:2444px;text-align:center;font-size:36px;font-weight:600;font-family:"IBM Plex Sans",Arial,sans-serif}
.card{top:2507px;width:271px;height:387px;background:#fff;box-shadow:0 6px 22px rgba(30,50,70,.08)}
.card .img{height:176px}
.card .body{padding:18px 30px}
.card .date{font-size:8px;font-weight:700;letter-spacing:1.5px;color:#c3cbd1}
.card h3{font-size:16px;line-height:21px;font-weight:600;margin:6px 0 14px;color:var(--ink)}
.card p{font-size:12px;line-height:20px;color:#3e474f;height:60px}
.link{font-size:12px;font-weight:700;color:var(--ink);border-bottom:2px solid var(--ink);padding-bottom:2px;display:inline-block}
.see-all{left:176px;top:2915px;font-size:13px}

/* cta */
.cta-sky{left:0;top:2958px;width:1200px;height:199px;background:linear-gradient(180deg,rgba(255,255,255,0),#e3e7eb)}
.footer{left:0;top:3157px;width:1200px;height:492px;background:var(--dark)}
.cta{top:3057px;height:207px;color:#fff;padding:42px 0 0 115px}
.cta h3{font-size:22px;line-height:28px;font-weight:600;width:240px}
.cta p{font-size:12px;line-height:20px;margin-top:10px;color:#e7eef5}
.cta .link{color:#fff;border-color:#fff;margin-top:12px}
.cta svg{position:absolute;left:40px;top:38px}

/* footer */
.f-brand{left:206px;top:3400px;font-size:40px;font-weight:600;color:#fff;font-family:"IBM Plex Sans",Arial,sans-serif;display:flex;align-items:center;gap:12px}
.f-brand .dot{width:18px;height:18px;border-radius:50%;background:var(--mint)}
.f-col{top:3368px;color:#cfd8de;font-size:12px;line-height:20px}
.f-col h4{font-family:"Karla",Arial,sans-serif;font-size:13px;font-weight:700;color:#fff;margin-bottom:10px}
.f-legal{left:207px;top:3592px;font-size:8px;color:#9aa7b0;line-height:14px}
.f-legal span{margin-right:14px}
.f-soc{top:3597px;width:10px;height:10px;border-radius:50%;background:#3a8fd4}
.f-line{left:0;top:3649px;width:1200px;height:14px;background:linear-gradient(90deg,#1a9a5a,#1c9ad6)}
</style>
</head>
<body>

<div class="abs topbar">Lorem ipsum dolor sit amet, consectetur adipiscing elit. <a>LEARN MORE</a></div>

<header>
  <div class="abs brand" style="left:166px;top:62px"><span class="dot"></span>ZolvantaRx</div>
  <span class="abs soc" style="left:725px"></span>
  <span class="abs soc" style="left:746px"></span>
  <span class="abs soc" style="left:767px"></span>
  <span class="abs util" style="left:829px">Careers</span>
  <span class="abs util" style="left:893px">Client Portal</span>
  <span class="abs util" style="left:981px">◍ ENG ▾</span>
  <nav>
    <span class="abs nav" style="left:418px">Home</span>
    <span class="abs nav" style="left:476px">Services</span>
    <span class="abs nav" style="left:550px">About Us</span>
    <span class="abs nav" style="left:628px">Industries</span>
    <span class="abs nav" style="left:714px">Contact Us</span>
  </nav>
  <svg class="abs search" viewBox="0 0 14 14"><circle cx="6" cy="6" r="4.5" fill="none" stroke="#1f2a33" stroke-width="1.6"/><line x1="9.3" y1="9.3" x2="13" y2="13" stroke="#1f2a33" stroke-width="1.6"/></svg>
  <div class="abs btn btn-dark" style="left:917px;top:75px;width:115px;height:39px">Get Started</div>
</header>

<section class="abs hero">
  <h1>Reshaping the Future &amp; Growth of Healthcare.</h1>
  <p>ZolvantaRx programs help patients achieve their therapeutic goals while cultivating growth and profitability for their clients.</p>
  <div class="btn btn-dark">Our Services</div>
  <div class="dashes"><span></span><span></span><span></span><span></span></div>
  <div class="hero-photo" role="img" aria-label="Photo of a smiling doctor in a white coat holding a clipboard"></div>
</section>
<div class="abs vtext" style="left:66px;top:476px;color:rgba(255,255,255,.7)">GET STARTED</div>
<div class="abs vline" style="left:70px;top:585px;height:200px"></div>

<section class="abs about">
  <div class="eyebrow">ABOUT US</div>
  <h2>Advanced technology solutions for healthcare organizations.</h2>
  <p>ZolvantaRx is an affordability program administrator representing Patient Service Programs (PSP) sponsored by manufacturers of drugs and other clinical products.<br>Connecting with all sites of care and removing all barriers with novel solutions, ZolvantaRx provides a Suite of Services that delivers progressive, efficient, and cost-effective PSP through advanced technology solutions to healthcare organizations.</p>
  <div class="btn">About Us</div>
</section>

<section class="abs services">
  <h2>Our Services</h2>
  <div class="abs skyline" role="img" aria-label="Faint line drawing of a city skyline"></div>

  <svg class="abs" style="left:400px;top:89px" width="400" height="400" viewBox="0 0 400 400" aria-label="Service wheel">
    <path d="M314.3 48.2 A190 190 0 0 1 390 203.3 L318 202.1 A118 118 0 0 0 271 105.7 Z" fill="#8fd3be"/>
    <path d="M389.3 216.6 A190 190 0 0 1 297.9 362.8 L260.8 301.1 A118 118 0 0 0 317.5 210.3 Z" fill="#25343d"/>
    <path d="M286.3 369.3 A190 190 0 0 1 113.7 369.3 L146.4 305.1 A118 118 0 0 0 253.6 305.1 Z" fill="#1f8f96"/>
    <path d="M102.1 362.8 A190 190 0 0 1 10.7 216.6 L82.5 210.3 A118 118 0 0 0 139.2 301.1 Z" fill="#6cc5a9"/>
    <path d="M10 203.3 A190 190 0 0 1 85.6 48.2 L129 105.7 A118 118 0 0 0 82 202.1 Z" fill="#4f76ad"/>
    <circle cx="200" cy="200" r="100" fill="#e1e3e6"/>
    <circle cx="200" cy="200" r="88" fill="#cfd2d6"/>
    <text x="200" y="208" text-anchor="middle" font-family="IBM Plex Sans, sans-serif" font-size="20" font-weight="600" fill="#1f2a33">ZolvantaRx</text>
    <g fill="none" stroke="#fff" stroke-width="2.4">
      <rect x="323" y="114" width="22" height="16" rx="2"/><rect x="334" y="126" width="18" height="13" rx="2"/>
      <rect x="303" y="272" width="18" height="24" rx="1"/><rect x="313" y="280" width="18" height="22" rx="1"/>
      <path d="M200 314 l14 5 v10 c0 9 -7 14 -14 17 c-7 -3 -14 -8 -14 -17 v-10 z"/><path d="M194 330 l5 5 l8 -9"/>
      <rect x="56" y="272" width="20" height="26" rx="1"/><circle cx="80" cy="294" r="6"/><line x1="84" y1="298" x2="90" y2="304"/>
      <rect x="54" y="108" width="22" height="28" rx="1"/><circle cx="65" cy="118" r="5"/><line x1="58" y1="130" x2="72" y2="130"/>
    </g>
    <line x1="0" y1="268" x2="-24" y2="280" stroke="#3a444c" stroke-width="1"/>
    <line x1="400" y1="270" x2="424" y2="282" stroke="#3a444c" stroke-width="1"/>
  </svg>

  <div class="abs svc r" style="left:118px;top:158px;width:235px">
    <h3>ZolvantaRx Claims<br>Processor®</h3>
    <p>Connects all sites of care, TWB represents solutions and advanced technology for real-time data, real-time benefit design changes, and custom benefit design options to support market access strategy at the patient and provider level.</p>
  </div>
  <div class="abs svc" style="left:846px;top:179px;width:255px">
    <h3>Advisory Services</h3>
    <p>Supports pharma sponsored PSP with innovative design and development solutions for Affordability Programs, Market Access Strategy, and addresses Compliance and Budgetary Management issues.</p>
  </div>
  <div class="abs svc r" style="left:137px;top:379px;width:250px">
    <h3>Robust Reporting</h3>
    <p>Reporting capabilities of all data fields captured from the claim submission in both pharmacy benefit and medical benefit programs. Customizable reports and data feeds to meet the needs of the program sponsor.</p>
  </div>
  <div class="abs svc" style="left:813px;top:379px;width:245px">
    <h3>POS Transaction Adjustments</h3>
    <p>Seamlessly recognize and address under reimbursement by primary payors. Avoid undesirable NDC substitution to competing brands because of insufficient reimbursement to pharmacy</p>
  </div>
  <div class="abs svc c" style="left:450px;top:530px;width:300px">
    <h3>Accumulator/Maximizer Defense</h3>
    <p>Accumulator / Maximizer defense through naïve solutions, proprietary algorithms, and customizable benefit designs. Real-time benefit adjustments to protect program sponsor funds while maintaining speed to therapy.</p>
  </div>
</section>

<section class="abs mission">
  <div class="mission-photo" role="img" aria-label="Photo of a confident doctor with arms crossed in a white coat"></div>
  <div class="eyebrow">OUR MISSION</div>
  <h2>We are Here to Make Running Healthcare Much Easier</h2>
  <p style="top:260px">Aliquam vitae purus nunc. Morbi ipsum ligula, auctor sit amet aliquet quis, viverra ut mauris. Aenean eget tempus sapien. Donec lobortis orci eget iaculis lorem ipsum finibus.</p>
  <p style="top:340px">Phasellus mollis feugiat turpis, et elementum est vehicula ornare accumsan. Praesent semper aliquet vitae fringilla. Etiam quis mauris dolor. Aliquam ultrices magna sit amet neque elementum, vel dapibus lectus sollicitudin.</p>
</section>

<h2 class="abs news-title">Latest News &amp; Resources</h2>

<article class="abs card" style="left:166px">
  <div class="img" role="img" aria-label="Photo of a team meeting around a desk in a bright office" style="background:linear-gradient(135deg,#e9ecef,#b9c2ca 60%,#6b7680)"></div>
  <div class="body"><div class="date">DEC 5, 2022</div><h3>Reinvent strategy to take advantage of future opportunities</h3><p>Mauris sagittis aliquet mi, nec gravida tellus molestie sem eros</p><span class="link">Read More</span></div>
</article>
<article class="abs card" style="left:465px">
  <div class="img" role="img" aria-label="Photo of two colleagues talking at a laptop" style="background:linear-gradient(135deg,#cfd6cf,#8c9a94 55%,#3f4a4a)"></div>
  <div class="body"><div class="date">DEC 5, 2022</div><h3>Think long-term value for your stakeholders</h3><p>Pellentesque mattis sollicitudin lorem ipsum mauris sagittis aliquet</p><span class="link">Read More</span></div>
</article>
<article class="abs card" style="left:762px">
  <div class="img" role="img" aria-label="Photo of two women chatting on a sofa" style="background:linear-gradient(135deg,#8fa98a,#cfc6bb 55%,#6d5a4e)"></div>
  <div class="body"><div class="date">DEC 5, 2022</div><h3>Post-Brexit UK: New homeland for new financial technologies?</h3><p>Pellentesque mattis sollicitudin lorem ipsum mauris sagittis aliquet</p><span class="link">Read More</span></div>
</article>
<span class="abs link see-all">See all Latest News</span>

<div class="abs cta-sky" role="img" aria-label="Faint line drawing of a city skyline"></div>
<footer class="abs footer"></footer>
<div class="abs vtext" style="left:66px;top:3060px;color:#9fb0bb">REACH OUT</div>
<div class="abs vline" style="left:70px;top:3140px;height:250px;background:rgba(255,255,255,.35)"></div>

<div class="abs cta" style="left:166px;width:421px;background:var(--cta-blue)">
  <svg width="56" height="48" viewBox="0 0 56 48"><path d="M2 22 L54 2 L40 46 L26 30 Z" fill="#fff"/><path d="M26 30 L54 2 L22 44 Z" fill="#dfe7f2"/></svg>
  <h3>Stay up to date with what matters</h3>
  <p>Get personalised content based on your interests direct to your inbox.</p>
  <span class="link">Sign up Today</span>
</div>
<div class="abs cta" style="left:613px;width:419px;background:var(--cta-teal)">
  <svg width="56" height="56" viewBox="0 0 56 56"><circle cx="22" cy="22" r="18" fill="#fff"/><text x="22" y="30" text-anchor="middle" font-size="22" font-weight="700" fill="#27979c" font-family="Karla, sans-serif">?</text><circle cx="40" cy="40" r="12" fill="#fff" stroke="#27979c" stroke-width="2"/><path d="M34 40 l4 4 l8 -8" fill="none" stroke="#27979c" stroke-width="2.4"/></svg>
  <h3>Got a question? Get in touch</h3>
  <p>Schedule your complimentary consultation.<br>We look forward to working with you.</p>
  <span class="link">Make an Enquiry</span>
</div>

<div class="abs f-brand"><span class="dot"></span>ZolvantaRx</div>

<div class="abs f-col" style="left:515px">
  <h4>Contact Us</h4>
  <div style="padding-left:22px;position:relative"><svg style="position:absolute;left:0;top:3px" width="11" height="14" viewBox="0 0 11 14"><path d="M5.5 0 C2.5 0 0 2.4 0 5.4 C0 9 5.5 14 5.5 14 S11 9 11 5.4 C11 2.4 8.5 0 5.5 0 Z" fill="#fff"/><circle cx="5.5" cy="5.3" r="2" fill="#25343d"/></svg>418 W. Harlow Ave. Suite 210<br>New York, NY 10014</div>
  <div style="padding-left:22px;position:relative;margin-top:20px"><svg style="position:absolute;left:0;top:4px" width="12" height="12" viewBox="0 0 12 12"><path d="M2 0 L4.5 3 L3 4.8 C4 7 5 8 7.2 9 L9 7.5 L12 10 L10 12 C4.5 11.5 0.5 7.5 0 2 Z" fill="#fff"/></svg>888-555-0142</div>
  <div style="padding-left:22px;position:relative"><svg style="position:absolute;left:0;top:6px" width="12" height="9" viewBox="0 0 12 9"><rect width="12" height="9" rx="1" fill="#fff"/><path d="M0.5 0.8 L6 5 L11.5 0.8" fill="none" stroke="#25343d" stroke-width="1.2"/></svg>info@zolvantarx-example.com</div>
</div>
<div class="abs f-col" style="left:775px">
  <h4>Resources</h4>Insights<br>From The Blog<br>Our Clients<br>Client Portal
</div>
<div class="abs f-col" style="left:921px">
  <h4>About Us</h4>About us<br>Contact us
</div>

<div class="abs f-legal"><span>Legal Notice</span><span>GDPR compliance</span><span>Privacy policy</span><span>Modern slavery statement</span><br>Copyright © 2023 – All rights reserved – Studio North</div>
<span class="abs f-soc" style="left:919px"></span>
<span class="abs f-soc" style="left:950px"></span>
<span class="abs f-soc" style="left:982px"></span>
<div class="abs f-line"></div>

</body>
</html>
```